Flyer-Design für Unterstützung bei Organisation
Zielgruppe
Ich begleite und unterstütze Organisationen und Menschen in Organisationen in ihren Veränderungs- Entwicklungs- und Problemlösungsprozessen ( Führungscoaching, Teamcoaching, Teamentwicklung). Meine Zielgruppe sind Personen in den Berufsrollen Geschäftsführer, HR-Verantwortliche, Führungspersonen, Mitarbeitende in Firmen.
Aufgabenstellung
Ich möchte die Flyer in einem Briefversan mitsenden, wo ich Firmen anschreibe und meine Dienstleistungen vorstelle. Auch möchte ich den Flyer an Orten auflegen, wo mein Zielpublikum Konsultationen in Anspruch nehmen könnte, bsp. Versicherungsagenturen, Hausarztpraxis, Physiotherapie etc.
kurz, interessant und ansprechend die Dienstleistungen gemäss Homepage beschreiben
https://www.lumowegweis.ch/firmen
DIN-Format: DIN A6/5 210 x 105 mm ist optional, lasse mich gerne auch von anderen Vorschlägen überraschen.

```html
<!DOCTYPE html>
<html lang="de">
<head>
<meta charset="utf-8">
<title>Lumowegweis – Flyer</title>
<link href="https://fonts.googleapis.com/css2?family=Barlow:wght@400;500;600;700&display=swap" rel="stylesheet">
<style>
  :root{
    --ink:#3a3a3a;
    --grey:#8f8f8f;
    --blue:#7ea7c8;
    --blue-text:#5f87a8;
    --red:#b8262a;
    --cream:#fcfae4;
    --cream-line:#f3ecb8;
    --white:#ffffff;
  }
  *{margin:0;padding:0;box-sizing:border-box}
  html,body{width:1200px;height:1200px;overflow:hidden;background:var(--white)}
  body{font-family:"Barlow",Arial,sans-serif;color:var(--ink)}
  .flyer{position:relative;width:1200px;height:1200px;overflow:hidden;background:var(--white)}
  .hero,.profile-wave{position:absolute;left:0;width:1200px}
  .hero{top:0;height:420px}
  .brand{position:absolute;display:flex;align-items:center;gap:14px;color:var(--grey);font-weight:500;letter-spacing:2px}
  .brand .dot{border-radius:50%;background:var(--blue);flex:none}
  .brand--top{left:82px;top:118px;font-size:36px}
  .brand--top .dot{width:26px;height:26px}
  .brand--footer{left:236px;top:1120px;font-size:21px;gap:8px;letter-spacing:1px}
  .brand--footer .dot{width:14px;height:14px}
  .badge{position:absolute;left:922px;top:275px;width:190px;height:190px;border-radius:50%;background:var(--white);border:8px solid var(--cream-line)}
  .headline{position:absolute;left:82px;top:415px;font-size:60px;line-height:62px;font-weight:400;color:var(--ink);letter-spacing:-.5px}
  .headline strong{font-weight:700}
  .profile{position:absolute;left:0;top:600px;width:1200px;height:420px;background:var(--cream)}
  .portrait{position:absolute;left:82px;top:117px;width:160px;height:160px;border-radius:50%;background:linear-gradient(135deg,#d9d6d2,#9a8f88);border:6px solid #c9d6e0}
  .profile-title{position:absolute;left:290px;top:122px;color:var(--blue-text);font-weight:700;font-size:26px;line-height:31px;letter-spacing:.5px}
  .person{position:absolute;left:290px;top:214px;font-size:15px;line-height:19px}
  .person .name{color:var(--red);font-weight:700;font-size:17px;margin-bottom:4px}
  .profile-text{position:absolute;left:558px;top:216px;width:532px;font-size:14.5px;line-height:22.5px}
  .profile-wave{top:900px;height:140px}
  .contact{position:absolute;left:469px;top:1098px;font-size:16px;line-height:24px;font-style:normal}
  .more{position:absolute;left:852px;top:1098px;font-size:16px;line-height:23px}
  .more .label{font-weight:700;text-transform:uppercase}
  .more .web{color:var(--red);font-weight:700;font-size:19px}
</style>
</head>
<body>
<div class="flyer">
  <svg class="hero" viewBox="0 0 1200 420">
    <defs>
      <linearGradient id="beach" x1="0" y1="0" x2="1" y2="0.4">
        <stop offset="0" stop-color="#ffffff"/>
        <stop offset="0.3" stop-color="#dfe8ea"/>
        <stop offset="0.45" stop-color="#d9a15e"/>
        <stop offset="1" stop-color="#cd7c2c"/>
      </linearGradient>
    </defs>
    <path role="img" aria-label="Foto: Fussspuren im Sand am Meeresufer" fill="url(#beach)" d="M0,0 H1200 V318 C900,375 420,372 0,292 Z"/>
    <path fill="var(--cream-line)" d="M0,288 C420,368 900,372 1200,312 V322 C900,382 420,378 0,298 Z"/>
    <path fill="var(--blue)" d="M0,298 C420,378 900,382 1200,322 V350 C900,400 420,398 0,322 Z"/>
  </svg>

  <div class="brand brand--top"><span class="dot"></span>LUMOWEGWEIS</div>

  <div class="badge" aria-hidden="true"></div>

  <h1 class="headline"><strong>Neue Wege</strong> entstehen,<br>indem <strong>wir sie gehen.</strong></h1>

  <section class="profile">
    <div class="portrait" role="img" aria-label="Porträtfoto der Coachin"></div>
    <h2 class="profile-title">LUMOWEGWEIS –<br>DAS BIN ICH</h2>
    <div class="person">
      <p class="name">SELINA WYSSMANN</p>
      <p>dipl. Coach SCA,<br>Betriebliche Mentorin FA</p>
    </div>
    <p class="profile-text">Als Coach, Mentorin und Trainerin mit eidgenössischem Fachausweis und Berufs­diplom, begleite ich Menschen bei den Problemlösungen in den Spannungsfeldern Privatleben, Beruf und Organisation - oder auch nur in einem dieser drei Bereiche.</p>
  </section>

  <svg class="profile-wave" viewBox="0 0 1200 140" aria-hidden="true">
    <path fill="var(--white)" d="M0,62 C400,118 850,118 1200,50 V140 H0 Z"/>
    <path fill="var(--cream-line)" d="M0,62 C400,118 850,118 1200,50 V58 C850,126 400,126 0,70 Z"/>
    <path fill="var(--blue)" d="M0,70 C400,126 850,126 1200,58 V82 C850,145 400,148 0,100 Z"/>
    <path fill="var(--cream-line)" d="M0,100 C400,148 850,145 1200,82 V88 C850,151 400,154 0,106 Z"/>
  </svg>

  <div class="brand brand--footer"><span class="dot"></span>LUMOWEGWEIS</div>

  <address class="contact">
    Mattenweg 17, CH - 3380 Wangenried<br>
    Telefon +41 79 000 48 26<br>
    Email info@lumowegweis.ch
  </address>

  <div class="more">
    <p class="label">Weitere Informationen</p>
    <p>finden Sie auf meiner Homepage</p>
    <p class="web">www.lumowegweis.ch</p>
  </div>
</div>
</body>
</html>
```